Brenton High 20 year Reunion Memorial

I need a tasteful memorial poster with the names of those alumni that have deceased. The school colors are black, orange, silver and white. I would definately like the background to be black. At the top of the poster I would like it to read:
Brenton Hight School Class of 1993.
This evening is dedicated in memory of
(followed by the names on the attached file

Industry/Entity Type

School

Requirements
Must have
• Black background

```html
<!DOCTYPE html>
<html lang="en">
<head>
<meta charset="utf-8">
<title>Brenton High School Class of 1993 – In Memory Of</title>
<link href="https://fonts.googleapis.com/css2?family=Libre+Baskerville:ital@0;1&display=swap" rel="stylesheet">
<style>
  :root {
    --night: #000000;
    --charcoal: #1c1c1e;
    --orange: #f28a24;
    --silver: #c8ccd2;
    --white: #ffffff;
  }
  html, body {
    margin: 0;
    padding: 0;
    overflow: hidden;
    background: var(--night);
  }
  .poster {
    position: relative;
    width: 775px;
    height: 1200px;
    overflow: hidden;
    color: var(--white);
    font-family: "Libre Baskerville", Baskerville, Georgia, serif;
    background:
      radial-gradient(ellipse 62% 50% at 45% 52%, var(--charcoal) 35%, rgba(0,0,0,0) 100%),
      linear-gradient(180deg, #2a1a0c 0%, var(--night) 22%, var(--night) 80%, #111112 100%);
  }
  .poster-title {
    position: absolute;
    top: 50px;
    left: 49px;
    margin: 0;
    font-weight: 400;
    font-size: 42.5px;
    line-height: 65px;
    color: var(--orange);
  }
  .poster-title .school-name,
  .poster-title .class-year {
    display: block;
    white-space: nowrap;
  }
  .poster-title .class-year {
    padding-left: 86px;
  }
  .dedication {
    position: absolute;
    top: 284px;
    left: 160px;
    margin: 0;
    font-weight: 400;
    font-size: 31px;
    color: var(--silver);
  }
  .memorial-list {
    position: absolute;
    top: 380px;
    left: 290px;
    margin: 0;
    padding: 0;
    list-style: none;
    font-style: italic;
    font-size: 24.5px;
    line-height: 38px;
  }
  .memorial-list li {
    margin-bottom: 34px;
  }
  .memorial-list .name,
  .memorial-list .dates {
    display: block;
    white-space: nowrap;
  }
  .memorial-list .name {
    color: var(--white);
  }
  .memorial-list .dates {
    color: var(--silver);
  }
</style>
</head>
<body>
  <main class="poster">
    <h1 class="poster-title">
      <span class="school-name">Brenton High School</span>
      <span class="class-year">Class of&nbsp; 1993</span>
    </h1>
    <h2 class="dedication">In Memory Of:</h2>
    <ul class="memorial-list">
      <li><span class="name">Carla Whitfield</span><span class="dates">May 7, 1975-November 28, 1993</span></li>
      <li><span class="name">Devin Marsh</span><span class="dates">April 29, 1975-June 10, 1997</span></li>
      <li><span class="name">Grant Ellery</span><span class="dates">April 22, 1975- April 2, 2002</span></li>
      <li><span class="name">Luis Moreno</span><span class="dates">August 28, 1975-February 27, 2010</span></li>
      <li><span class="name">Tessa Lindqvist</span><span class="dates">July 13, 1975-October 5, 2011</span></li>
      <li><span class="name">Paige Holloway</span><span class="dates">January 26, 1975-December 22, 2012</span></li>
      <li><span class="name">Kyle Brannigan</span><span class="dates">April 29, 1975- January 30, 2013</span></li>
    </ul>
  </main>
</body>
</html>
```